I want a website for a digital media and music production company named brackenhale media

I want a website e commerce, that showcases our experience and projects, and sells merchandise and others.
we will use ai, produce webcasts, podcasts, musical talent.
we have the recording studios staff and equipment to produce and manage talent. We are an influencer factory and top content producers for social media radio and tv.
Must be able to stream video, podcasts, monetize, and have pay to view options.
we need a content manage system to change , upload video and images content constantly-

```html
<!DOCTYPE html>
<html lang="en">
<head>
<meta charset="utf-8">
<title>Brackenhale Media</title>
<link href="https://fonts.googleapis.com/css2?family=Open+Sans:wght@400;600;700&display=swap" rel="stylesheet">
<style>
  :root {
    --white: #ffffff;
    --bg-dark: #121a21;
    --bg-mid: #2a4152;
    --bg-light: #5d7383;
    --accent-start: #0a6cbf;
    --accent-end: #5cc3df;
  }
  * { margin: 0; padding: 0; box-sizing: border-box; }
  html, body { width: 1200px; height: 675px; overflow: hidden; background: var(--bg-dark); }
  body { font-family: "Open Sans", sans-serif; color: var(--white); }
  .hero { position: relative; width: 1200px; height: 675px; overflow: hidden; }
  .hero-backdrop {
    position: absolute; inset: 0;
    background:
      radial-gradient(ellipse 520px 300px at 600px 40px, rgba(160,178,190,0.55), transparent 70%),
      radial-gradient(ellipse 420px 260px at 600px 420px, rgba(80,110,132,0.45), transparent 75%),
      radial-gradient(ellipse 160px 120px at 320px 550px, rgba(40,90,130,0.35), transparent 80%),
      radial-gradient(ellipse 140px 110px at 830px 430px, rgba(40,90,130,0.3), transparent 80%),
      linear-gradient(180deg, var(--bg-mid) 0%, #1f3140 55%, var(--bg-dark) 100%);
  }
  .site-header { position: absolute; top: 0; left: 0; width: 1200px; height: 130px; }
  .brand {
    position: absolute; left: 94px; top: 62px;
    display: flex; align-items: center; gap: 8px;
    font-size: 15px; font-weight: 700; letter-spacing: 1.5px; text-transform: uppercase;
  }
  .brand-mark { width: 12px; height: 12px; background: var(--white); }
  .main-nav { position: absolute; left: 498px; top: 68px; display: flex; gap: 25px; }
  .main-nav a { color: var(--white); text-decoration: none; font-size: 12.5px; line-height: 18px; }
  .btn {
    display: flex; align-items: center; justify-content: center;
    width: 137px; height: 31px; font-size: 12.5px; font-weight: 600;
    color: var(--white); text-decoration: none; text-transform: uppercase;
  }
  .btn-outline { border: 1.5px solid var(--white); }
  .btn-fill { background: linear-gradient(90deg, var(--accent-start), var(--accent-end)); }
  .header-actions { position: absolute; left: 807px; top: 62px; display: flex; gap: 25px; }
  .hero-content { position: absolute; left: 0; top: 214px; width: 1200px; text-align: center; }
  .eyebrow {
    position: relative; font-size: 20px; font-weight: 600; letter-spacing: 2px; line-height: 30px;
  }
  .eyebrow-rule { position: absolute; top: 13px; width: 119px; height: 5px; }
  .eyebrow-rule.left { left: 384px; }
  .eyebrow-rule.right { left: 697px; }
  .hero-title { font-size: 52px; font-weight: 700; line-height: 62px; margin-top: 4px; letter-spacing: 0.5px; }
  .tagline { font-size: 20px; font-weight: 700; line-height: 26px; margin-top: 15px; }
  .intro { font-size: 19px; line-height: 22.5px; margin-top: 2px; }
  .hero-actions { display: flex; justify-content: center; gap: 32px; margin-top: 23px; }
</style>
</head>
<body>
<main class="hero">
  <div class="hero-backdrop" role="img" aria-label="Dim stage photograph of a vintage studio microphone under a soft spotlight"></div>

  <header class="site-header">
    <div class="brand"><span class="brand-mark"></span>Brackenhale Media</div>
    <nav class="main-nav">
      <a href="#">HOME</a>
      <a href="#">ABOUT</a>
      <a href="#">SERVICES</a>
      <a href="#">WORK</a>
    </nav>
    <div class="header-actions">
      <a class="btn btn-outline" href="#">Get in touch</a>
      <a class="btn btn-fill" href="#">Request a quote</a>
    </div>
  </header>

  <section class="hero-content">
    <div class="eyebrow">
      <svg class="eyebrow-rule left" viewBox="0 0 119 5" preserveAspectRatio="none"><polygon points="0,2.5 119,0 119,5" fill="#ffffff"/></svg>
      WELCOME TO
      <svg class="eyebrow-rule right" viewBox="0 0 119 5" preserveAspectRatio="none"><polygon points="0,0 119,2.5 0,5" fill="#ffffff"/></svg>
    </div>
    <h1 class="hero-title">BRACKENHALE MEDIA</h1>
    <p class="tagline">Transforming Creativity</p>
    <p class="intro">Explore Our AI-Driven Webcasts, Podcasts,<br>and Musical Innovations</p>
    <div class="hero-actions">
      <a class="btn btn-fill" href="#">Request a quote</a>
      <a class="btn btn-outline" href="#">Get in touch</a>
    </div>
  </section>
</main>
</body>
</html>
```